Criação de Power Point Slide Mestre para Consultoria de Negócios
" Venda de serviços de consultoria e treinamentos. Atende clientes com foco na melhoria da gestão através de metodologia de gestão e foco em melhoria do resultado operacional e consequentemente financeiro das empresas. "

```html
<!DOCTYPE html>
<html lang="pt-BR">
<head>
<meta charset="UTF-8">
<title>Serviços Oferecidos – Slide Mestre</title>
<link rel="stylesheet" href="https://fonts.googleapis.com/css2?family=Montserrat:wght@600;700&family=Open+Sans:wght@400;600&display=swap">
<style>
  :root {
    --page-bg: #e4e7ea;
    --slide-bg: #f3f4f5;
    --navy: #1f2d3d;
    --navy-deep: #16222f;
    --gold: #c9a24a;
    --gold-dark: #8f6e2a;
    --text: #3b4450;
    --white: #ffffff;
  }
  * { margin: 0; padding: 0; box-sizing: border-box; }
  html, body {
    width: 1200px; height: 1200px; overflow: hidden;
    background: var(--page-bg);
  }
  .slide {
    position: absolute; left: 40px; top: 285px;
    width: 1120px; height: 630px;
    background: var(--slide-bg);
    overflow: hidden;
    box-shadow: 0 10px 40px rgba(0,0,0,.15);
  }
  .slide-shapes { position: absolute; inset: 0; }
  .slide-title {
    position: absolute; left: 62px; top: 84px;
    font-family: 'Montserrat', sans-serif; font-weight: 700;
    font-size: 30px; letter-spacing: 1px; color: var(--white);
  }
  .service-list {
    position: absolute; left: 62px; top: 168px;
    list-style: none;
    font-family: 'Open Sans', sans-serif; font-weight: 600;
    font-size: 18px; color: var(--text);
  }
  .service-list li {
    display: flex; align-items: center; gap: 12px;
    height: 35px;
  }
  .service-list li::before {
    content: ""; width: 13px; height: 13px; border-radius: 50%;
    background: radial-gradient(circle at 35% 35%, var(--gold), var(--gold-dark));
    flex: none;
  }
  .brand {
    position: absolute; right: 80px; bottom: 48px;
    display: flex; align-items: center; gap: 14px;
    font-family: 'Montserrat', sans-serif; font-weight: 600;
    font-size: 34px; letter-spacing: 2px; color: var(--white);
  }
  .brand-mark { width: 26px; height: 26px; background: var(--gold); }
</style>
</head>
<body>
  <section class="slide">
    <svg class="slide-shapes" width="1120" height="630" viewBox="0 0 1120 630">
      <defs>
        <linearGradient id="photo-tone" x1="0" y1="0" x2="1" y2="0.3">
          <stop offset="0" stop-color="#dfe4ea"/>
          <stop offset="0.45" stop-color="#a9b4c2"/>
          <stop offset="1" stop-color="#2a3850"/>
        </linearGradient>
      </defs>
      <polygon class="photo-area" role="img"
        aria-label="Foto de executivo de terno marcando caixas de seleção com caneta"
        points="640,0 1120,0 1120,500 560,500" fill="url(#photo-tone)"/>
      <polygon class="title-band" points="40,70 560,70 530,132 40,132" fill="var(--navy)"/>
      <polygon class="title-accent" points="40,136 527,136 524,142 40,142" fill="var(--gold)"/>
      <polygon class="brand-band" points="600,500 1120,470 1120,630 540,630" fill="var(--navy-deep)"/>
      <polygon class="brand-accent" points="600,500 1120,470 1120,476 597,506" fill="var(--gold)"/>
    </svg>

    <h1 class="slide-title">SERVIÇOS OFERECIDOS</h1>

    <ul class="service-list">
      <li>Gestão da Receita</li>
      <li>Gestão da Despesa</li>
      <li>Gestão Orçamentária</li>
      <li>Desdobramento de Metas - GPD</li>
      <li>Gestão de Indicadores de Rotina e Processos</li>
      <li>Gestão de Processos</li>
      <li>Gestão da Qualidade do Serviço Prestado</li>
      <li>Gestão para Varejo</li>
      <li>Ferramentas de Gestão Customizadas</li>
      <li>Gestão dos Planos de Ação</li>
      <li>Treinamentos</li>
    </ul>

    <div class="brand">
      <span class="brand-mark"></span>
      <span class="brand-name">NORVIA</span>
    </div>
  </section>
</body>
</html>
```